Option Sheet

We need a one page option sheet with a left to right reading of the five options. It should be a one sheet, multiple colors and definitive separations between options This is used in a sales consultation. Backround or colors not in option need to have the follow RGB value (5 red, 20 green, 63 blue)

We added a smaller text file, please change that point

Target Market(s)

Divorce

Industry/Entity Type

Legal

Requirements
Must have
• 1) All five options left to right
• 2)language included in sheet

```html
<!DOCTYPE html>
<html lang="en">
<head>
<meta charset="utf-8">
<title>Divorce – Five Options</title>
<link href="https://fonts.googleapis.com/css2?family=Source+Sans+3:wght@400;600;700&display=swap" rel="stylesheet">
<style>
  :root {
    --backdrop: #6d6e71;
    --sheet-body: #c8d5d5;
    --brand-red: #ef4136;
    --opt-red: #ef4136;
    --opt-purple: #662d91;
    --opt-orange: #f7941d;
    --opt-green: #006838;
    --opt-blue: #27aae1;
    --text: #3a3a3a;
    --white: #ffffff;
  }
  * { box-sizing: border-box; margin: 0; padding: 0; }
  html, body {
    width: 1200px; height: 866px; overflow: hidden;
    background: var(--backdrop);
    font-family: "Source Sans 3", Arial, sans-serif;
    color: var(--text);
  }
  .option-sheet {
    position: absolute; left: 115px; top: 122px;
    width: 977px; height: 622px;
    background: var(--sheet-body);
  }
  .sheet-header {
    height: 100px; background: var(--brand-red);
    display: flex; align-items: center; justify-content: center;
  }
  .sheet-title {
    color: var(--white); font-weight: 400; font-size: 42px; letter-spacing: 0.5px;
  }
  .sheet-footer {
    position: absolute; left: 0; right: 0; bottom: 0; height: 8px;
    background: var(--brand-red);
  }
  .option-row {
    position: absolute; left: 12px; top: 143px;
    display: flex; gap: 6px;
  }
  .option-card {
    --accent: var(--opt-red);
    position: relative; width: 185px; height: 421px;
  }
  .option-card--purple { --accent: var(--opt-purple); }
  .option-card--orange { --accent: var(--opt-orange); }
  .option-card--green { --accent: var(--opt-green); }
  .option-card--blue { --accent: var(--opt-blue); }
  .card-body {
    position: absolute; left: 0; right: 0; top: 21px; bottom: 0;
    background: linear-gradient(90deg, #ececee 0%, #ffffff 35%, #ffffff 70%, #ededef 100%);
    border-radius: 14px 14px 10px 10px;
    overflow: hidden;
    padding: 44px 12px 0 9px;
  }
  .card-body::after {
    content: ""; position: absolute; left: 0; right: 0; bottom: 0; height: 9px;
    background: var(--accent);
  }
  .card-tab {
    position: absolute; left: 17px; width: 150px; top: 0; height: 49px;
    background: var(--accent); border-radius: 12px 12px 0 0;
    color: var(--white); text-align: center; padding-top: 7px;
  }
  .tab-number { font-weight: 700; font-size: 13.5px; line-height: 15px; display: block; }
  .tab-label { font-weight: 400; font-size: 12.5px; line-height: 15px; display: block; }
  .list-heading {
    color: var(--accent); font-weight: 700; font-size: 11.5px;
    text-align: center; margin: 8px 0 5px; letter-spacing: 0.2px;
  }
  .point-list { list-style: none; font-size: 11px; line-height: 13px; }
  .point-list li { padding-left: 7px; text-indent: -7px; margin-bottom: 5px; }
  .point-list li::before { content: "• "; }
  .divider {
    border: 0; border-top: 1px dotted var(--accent);
    margin: 9px 4px 10px; opacity: 0.8;
  }
</style>
</head>
<body>
<main class="option-sheet">
  <header class="sheet-header"><h1 class="sheet-title">DIVORCE - FIVE OPTIONS</h1></header>

  <section class="option-row">
    <article class="option-card option-card--red">
      <div class="card-body">
        <h3 class="list-heading">ADVANTAGES:</h3>
        <ul class="point-list"><li>Stay married</li><li>No life Changes</li></ul>
        <hr class="divider">
        <h3 class="list-heading">DISADVANTAGES:</h3>
        <ul class="point-list">
          <li>Remain unhappy, depressed, anxious</li>
          <li>Feel unsafe</li>
          <li>Money and assets may disappear</li>
          <li>Spouse may threaten to leave and/or divorce you</li>
          <li>May cause children to be confused, distressed</li>
          <li>What is going to change?</li>
        </ul>
      </div>
      <div class="card-tab"><span class="tab-number">OPTION #1</span><span class="tab-label">Do Nothing</span></div>
    </article>

    <article class="option-card option-card--purple">
      <div class="card-body">
        <h3 class="list-heading">ADVANTAGES:</h3>
        <ul class="point-list"><li>Reconcile marriage</li><li>Help make a better life</li></ul>
        <hr class="divider">
        <h3 class="list-heading">DISADVANTAGES:</h3>
        <ul class="point-list">
          <li>Past issues are highlighted and may drudge up old wounds</li>
          <li>It may just clarify the reasons you need to separate and/or divorce</li>
          <li>There is no quick fix for any situation and BOTH parties must be invested and willing to participate</li>
          <li>Bringing a third party into the marriage may cause more confusion and possible distrust</li>
        </ul>
      </div>
      <div class="card-tab"><span class="tab-number">OPTION #2</span><span class="tab-label">Go to Counseling</span></div>
    </article>

    <article class="option-card option-card--orange">
      <div class="card-body">
        <h3 class="list-heading">ADVANTAGES:</h3>
        <ul class="point-list"><li>No attorney fees</li></ul>
        <hr class="divider" style="margin-top:22px">
        <h3 class="list-heading">DISADVANTAGES:</h3>
        <ul class="point-list">
          <li>People often find that what is “fair,” may in fact, not be truly fair</li>
          <li>Often times, people do not know the risks</li>
          <li>Complicated legal system</li>
          <li>Unsure how to complete the necessary paperwork and meet the deadlines</li>
          <li>You are too emotional and may be unable to remain clear-headed</li>
          <li>It can be very stressful</li>
        </ul>
      </div>
      <div class="card-tab"><span class="tab-number">OPTION #3</span><span class="tab-label">Do it Yourself</span></div>
    </article>

    <article class="option-card option-card--green">
      <div class="card-body">
        <h3 class="list-heading">ADVANTAGES:</h3>
        <ul class="point-list"><li>Balance between going alone and our limited involvement in the case</li></ul>
        <h3 class="list-heading" style="margin-top:12px">DISADVANTAGES:</h3>
        <ul class="point-list">
          <li>Our terms may not benefit from our legal knowledge</li>
          <li>The legal consequences of your legal documents will not be explained to you so that you can formulate a plan for handling the rest of your case.</li>
          <li>Your spouse or other parties may cause your legal fees to increase significantly without action on your part</li>
        </ul>
      </div>
      <div class="card-tab"><span class="tab-number">OPTION #4</span><span class="tab-label">Limited Representation</span></div>
    </article>

    <article class="option-card option-card--blue">
      <div class="card-body">
        <h3 class="list-heading">ADVANTAGES:</h3>
        <ul class="point-list">
          <li>Provide peace of mind</li>
          <li>Often saves you money in the long run</li>
          <li>Can stop problems before they start and advise how actions /events may impact your case</li>
          <li>May be able to come to a settlement agreement sooner</li>
          <li>Lessen the emotional stress of one of the worst things that can happen to a person</li>
          <li>Inform you of your rights and what you are entitled to</li>
          <li>Save you time and energy</li>
          <li>Gain the full benefits of our experience</li>
          <li>Provide a shoulder to lean on and a sounding board</li>
        </ul>
        <hr class="divider">
        <h3 class="list-heading">DISADVANTAGES:</h3>
        <ul class="point-list"><li>Cost</li></ul>
      </div>
      <div class="card-tab"><span class="tab-number">OPTION #5</span><span class="tab-label">Hire Us</span></div>
    </article>
  </section>

  <div class="sheet-footer"></div>
</main>
</body>
</html>
```